RM Straßenlogistik Kundenflyer
Zielgruppe
Wir sind ein Verkehrssicherheitsdienstleister aus der Region Heilbronn und Umgebung. Zu unseren Kunden zählen z.B. Bauunternehmen, Dachdecker, Kellerbauer, Kranfirmen, Hausbauer, Holzbauer und Privatpersonen.
Leistungen:
Erstellen von Verkehrszeichenplänen
Einholen von Genehmigungen
Stellen von Straßensperrungen und Parkverboten
Vermietung von Verkehrszeichen
Aufgabenstellung
Aussagekräftige Bilder, nicht zu viel Text. Die Farbe der Verkehrssicherung ist Rot. Daher sollte der Flyer Weiß / Rot sein. kurze Beschreibung unserer Leistungen.

```html
<!DOCTYPE html>
<html lang="de">
<head>
<meta charset="utf-8">
<title>RM Straßenlogistik – Kundenflyer</title>
<link href="https://fonts.googleapis.com/css2?family=Jost:ital,wght@0,400;0,500;0,800;1,400&display=swap" rel="stylesheet">
<style>
  :root{
    --backdrop:#d9dcdf;
    --paper:#eef3fa;
    --red:#e32b24;
    --red-dark:#d8241f;
    --blush:#f2c4c1;
    --ink:#111111;
    --white:#ffffff;
  }
  *{box-sizing:border-box;margin:0;padding:0}
  html,body{width:803px;height:1200px;overflow:hidden;background:var(--backdrop);font-family:'Jost',sans-serif;color:var(--ink)}
  .sheet{position:absolute;top:242px;width:334px;height:716px;overflow:hidden}
  .sheet--front{left:42px;background:var(--paper)}
  .sheet--back{left:425px;background:var(--red)}
  .layer{position:absolute;left:0;top:0}

  /* front */
  .brand{position:absolute;display:flex;align-items:center;gap:7px;font-weight:800;font-size:19px;line-height:1}
  .brand__mark{width:14px;height:14px;background:currentColor;border-radius:2px}
  .sheet--front .brand{left:18px;top:40px;color:var(--red)}
  .headline{position:absolute;left:19px;top:134px;font-weight:800;font-size:25px;line-height:28px;letter-spacing:.2px}
  .tagline{position:absolute;left:20px;top:193px;font-style:italic;font-size:14px}
  .services__title{position:absolute;left:19px;top:243px;font-size:12.5px}
  .service{position:absolute;left:0;display:flex;align-items:center;font-size:12px;line-height:17px}
  .service__tab{height:32px;background:var(--ink);border-radius:0 7px 7px 0;display:flex;align-items:center;justify-content:flex-end;padding-right:9px;margin-right:6px;flex:none}
  .service__text b{font-weight:500}
  .lamp-photo{position:absolute;left:140px;top:452px;width:194px;height:192px}
  .footer{position:absolute;left:0;bottom:0;width:334px;background:var(--ink);color:var(--white)}
  .sheet--front .footer{height:73px;text-align:center;font-size:9.5px;line-height:13px;padding-top:16px}

  /* back */
  .street-photo{position:absolute;left:0;top:0}
  .closing{position:absolute;left:27px;top:386px;color:var(--white);font-weight:800;font-size:26px;line-height:29px;letter-spacing:.3px}
  .contacts{position:absolute;left:27px;top:464px;list-style:none;color:var(--white);font-size:13px;line-height:17px}
  .contacts li{display:flex;align-items:flex-start;gap:10px;margin-bottom:5px}
  .contacts svg{flex:none;margin-top:-1px}
  .sheet--back .footer{height:124px}
  .sheet--back .brand{left:26px;top:48px;color:var(--white)}
</style>
</head>
<body>

<section class="sheet sheet--front">
  <svg class="layer" width="334" height="716" viewBox="0 0 334 716" aria-hidden="true">
    <path d="M296 0 L334 0 L334 644 L0 644 L0 610 C120 600 262 500 282 330 C296 200 292 90 296 0 Z" fill="var(--blush)" opacity=".8"/>
    <path d="M302 0 L334 0 L334 644 L0 644 L0 622 C130 612 275 510 292 335 C305 205 300 90 302 0 Z" fill="var(--red)"/>
  </svg>

  <div class="brand"><span class="brand__mark"></span>RM Straßenlogistik</div>

  <h1 class="headline">Ihre Experten für<br>Verkehrssicherung!</h1>
  <p class="tagline">Sicher. Schnell. Zuverlässig.</p>

  <p class="services__title">Unsere Leistungen</p>
  <div class="service" style="top:272px"><span class="service__tab" style="width:29px"><svg width="14" height="14" viewBox="0 0 14 14"><path d="M2 7.5 L5.5 11 L12 2.5" stroke="#fff" stroke-width="2" fill="none"/></svg></span><span class="service__text"><b>Verkehrszeichenpläne</b> – Detaillierte<br>Planung für sichere Baustellen</span></div>
  <div class="service" style="top:316px"><span class="service__tab" style="width:47px"><svg width="14" height="14" viewBox="0 0 14 14"><path d="M2 7.5 L5.5 11 L12 2.5" stroke="#fff" stroke-width="2" fill="none"/></svg></span><span class="service__text"><b>Straßensperrungen &amp; Parkverbote</b> –<br>Sicher und professionell umgesetzt</span></div>
  <div class="service" style="top:360px"><span class="service__tab" style="width:65px"><svg width="14" height="14" viewBox="0 0 14 14"><path d="M2 7.5 L5.5 11 L12 2.5" stroke="#fff" stroke-width="2" fill="none"/></svg></span><span class="service__text"><b>Genehmigungen</b> – Behördliche<br>Anträge schnell &amp; unkompliziert</span></div>
  <div class="service" style="top:404px"><span class="service__tab" style="width:82px"><svg width="14" height="14" viewBox="0 0 14 14"><path d="M2 7.5 L5.5 11 L12 2.5" stroke="#fff" stroke-width="2" fill="none"/></svg></span><span class="service__text"><b>Verkehrszeichen-Vermietung</b> –<br>Lösungen für jedes Projekt.</span></div>

  <svg class="lamp-photo" viewBox="0 0 194 192" role="img" aria-label="Foto: rote Baustellen-Warnleuchten mit orangefarbenen Linsen auf Absperrbaken">
    <defs>
      <radialGradient id="lampGlow" cx="45%" cy="30%" r="75%">
        <stop offset="0" stop-color="#f7a21b"/>
        <stop offset=".45" stop-color="#e8432a"/>
        <stop offset="1" stop-color="#d8241f"/>
      </radialGradient>
    </defs>
    <path d="M60 0 C120 -6 194 10 194 10 L194 192 L0 192 L0 150 C20 90 30 20 60 0 Z" fill="url(#lampGlow)"/>
  </svg>

  <svg class="layer" width="334" height="716" viewBox="0 0 334 716" aria-hidden="true">
    <path d="M58 453 C40 470 28 500 45 515 C70 535 140 525 150 570 C155 595 140 620 125 630" stroke="var(--ink)" stroke-width="4" fill="none" stroke-linecap="round"/>
    <path d="M118 618 L120 641 L138 628 Z" fill="var(--ink)"/>
  </svg>

  <footer class="footer">
    kontakt@rm-strassenlogistik.de<br>www.rm-strassenlogistik.de<br>07131 5550190
  </footer>
</section>

<section class="sheet sheet--back">
  <svg class="street-photo" width="334" height="370" viewBox="0 0 334 370" role="img" aria-label="Foto: Umleitungsschild mit Ortstafel am Straßenrand, dahinter ein weißer Firmentransporter">
    <defs>
      <linearGradient id="streetTone" x1="0" y1="0" x2="0" y2="1">
        <stop offset="0" stop-color="#b3c9e6"/>
        <stop offset=".55" stop-color="#c9d3dd"/>
        <stop offset="1" stop-color="#8c8f92"/>
      </linearGradient>
    </defs>
    <path d="M0 0 L282 0 C272 190 190 330 0 360 Z" fill="url(#streetTone)"/>
    <path d="M282 0 L288 0 C280 195 196 336 0 366 L0 360 C190 330 272 190 282 0 Z" fill="var(--blush)" opacity=".7"/>
  </svg>

  <h2 class="closing">Wir freuen uns auf<br>Ihre Anfrage!</h2>

  <ul class="contacts">
    <li>
      <svg width="20" height="20" viewBox="0 0 20 20" aria-hidden="true"><rect width="20" height="20" rx="3" fill="var(--ink)"/><path d="M10 4.5a3.5 3.5 0 0 1 3.5 3.5c0 2.6-3.5 6-3.5 6s-3.5-3.4-3.5-6A3.5 3.5 0 0 1 10 4.5z" stroke="#fff" stroke-width="1.2" fill="none"/><circle cx="10" cy="8" r="1.2" fill="#fff"/><path d="M5 15.5h10" stroke="#fff" stroke-width="1.2"/></svg>
      <span>Am Lindenweg 8,<br>74076 Heilbronn</span>
    </li>
    <li style="margin-top:4px">
      <svg width="20" height="20" viewBox="0 0 20 20" aria-hidden="true"><rect width="20" height="20" rx="3" fill="var(--ink)"/><circle cx="10" cy="10" r="5.5" stroke="#fff" stroke-width="1.1" fill="none"/><ellipse cx="10" cy="10" rx="2.4" ry="5.5" stroke="#fff" stroke-width="1.1" fill="none"/><path d="M4.5 10h11" stroke="#fff" stroke-width="1.1"/></svg>
      <span>kontakt@rm-strassenlogistik.de</span>
    </li>
    <li>
      <svg width="20" height="20" viewBox="0 0 20 20" aria-hidden="true"><rect width="20" height="20" rx="3" fill="var(--ink)"/><rect x="4.5" y="6" width="11" height="8" rx="1" stroke="#fff" stroke-width="1.1" fill="none"/><path d="M4.5 6.5 L10 10.5 L15.5 6.5" stroke="#fff" stroke-width="1.1" fill="none"/></svg>
      <span>www.rm-strassenlogistik.de</span>
    </li>
    <li>
      <svg width="20" height="20" viewBox="0 0 20 20" aria-hidden="true"><rect width="20" height="20" rx="3" fill="var(--ink)"/><path d="M6 4.5 L8 4.5 L9 7.5 L7.5 8.7 C8.3 10.4 9.6 11.7 11.3 12.5 L12.5 11 L15.5 12 L15.5 14 C15.5 14.8 14.8 15.5 14 15.5 C9 15.2 4.8 11 4.5 6 C4.5 5.2 5.2 4.5 6 4.5 Z" stroke="#fff" stroke-width="1.1" fill="none"/></svg>
      <span>07131 5550190</span>
    </li>
  </ul>

  <footer class="footer">
    <div class="brand"><span class="brand__mark"></span>RM Straßenlogistik</div>
  </footer>
</section>

</body>
</html>
```